Roofing Company needs Business card design

We need a business card design for our roofing contracting company. We do Residential and commercial roofing. Design need to be modern, professional and clean. The design should communicate quality and professionalism. We would like to have rounded corners, but open to your ideas.
Company Name: Kestrel roofing Solutions
Company Address: (dummy text)
Name on business card: (dummy text)
And following lines:
Storm damage specialists
commercial & residential
shingles, flat and metal roofs./
Open to background colors.
I have ai. and eps files of logo if needed.
just let me know.
Target Market(s)
Mostly residential customers but we do commercial too.
Industry/Entity Type
Roofing
Look and feel

```html
<!DOCTYPE html>
<html lang="en">
<head>
<meta charset="UTF-8">
<title>Kestrel roofing Solutions – Business Card</title>
<link href="https://fonts.googleapis.com/css2?family=Montserrat:wght@400;500;600&display=swap" rel="stylesheet">
<style>
  :root {
    --backdrop: #ece9e4;
    --card-black: #0b0b0b;
    --card-black-soft: #262626;
    --card-red: #e41e26;
    --card-red-light: #f3474d;
    --ink-white: #ffffff;
    --ink-white-soft: rgba(255,255,255,0.88);
  }
  * { box-sizing: border-box; margin: 0; padding: 0; }
  html, body {
    width: 1200px; height: 900px; overflow: hidden;
    background: var(--backdrop);
    font-family: "Montserrat", sans-serif;
  }
  .stage {
    position: relative; width: 1200px; height: 900px;
    display: flex; align-items: center; justify-content: center; gap: 48px;
  }
  .card {
    position: relative; width: 520px; height: 297px;
    border-radius: 26px; overflow: hidden;
    box-shadow: 0 14px 30px rgba(0,0,0,0.22);
    color: var(--ink-white);
  }
  .card-front {
    background: linear-gradient(145deg, var(--card-black-soft) 0%, var(--card-black) 55%);
  }
  .brand {
    position: absolute; left: 50%; top: 50%;
    transform: translate(-50%, -50%);
    display: flex; align-items: center; gap: 16px;
    white-space: nowrap;
  }
  .brand-mark {
    width: 18px; height: 18px; background: var(--card-red);
  }
  .brand-name {
    font-weight: 500; font-size: 27px; letter-spacing: 0.06em;
    color: var(--ink-white);
  }
  .card-back {
    background: linear-gradient(160deg, var(--card-red-light) 0%, var(--card-red) 45%, #d3141c 100%);
  }
  .address {
    position: absolute; top: 26px; right: 30px;
    text-align: right; font-weight: 500; font-size: 14px;
    line-height: 1.3; letter-spacing: 0.04em; text-transform: uppercase;
  }
  .contact {
    position: absolute; left: 32px; top: 122px;
    font-size: 15px; line-height: 1.32;
  }
  .contact-name { font-weight: 500; font-size: 17px; letter-spacing: 0.03em; text-transform: uppercase; }
  .contact-role { font-weight: 400; }
  .services {
    position: absolute; left: 26px; right: 26px; bottom: 20px;
    display: flex; justify-content: space-between;
    font-size: 8.5px; font-weight: 500; letter-spacing: 0.08em;
    text-transform: uppercase; color: var(--ink-white-soft);
  }
</style>
</head>
<body>
  <main class="stage">
    <section class="card card-front" aria-label="Card front">
      <div class="brand">
        <span class="brand-mark"></span>
        <span class="brand-name">Kestrel roofing Solutions</span>
      </div>
    </section>

    <section class="card card-back" aria-label="Card back">
      <address class="address" style="font-style:normal">
        Street No,<br>Town,<br>City,<br>Zipcode
      </address>
      <div class="contact">
        <p class="contact-name">Daniel Reed</p>
        <p class="contact-role">Designation</p>
        <p class="contact-phone">123-456-7890</p>
        <p class="contact-email">daniel@kestrelroof.com</p>
      </div>
      <ul class="services" style="list-style:none">
        <li>Storm damage specialists</li>
        <li>Commercial &amp; residential</li>
        <li>Shingles, flat and metal roofs.</li>
      </ul>
    </section>
  </main>
</body>
</html>
```